New business card/stationary for a consulting company

I am looking for a clean and very professional looking business card for my consulting company as well as corresponding stationary. I am uploading our logo. I like simple and powerful for the feel. No graphics but I am open on everything else. Below is my contact information but would like the final to be in a version I can add my employees information into and print. Thank you.

Daniel Whitcombe
dan@fernlowadvisory.com
2837 North 9th Avenue, Summit Floor, Ashford Lake, Wisconsin 60483
www.fernlowadvisory.com

Industry/Entity Type

Consulting

Contact Information for Business Card

Daniel Whitcombe
dan@fernlowadvisory.com
www.fernlowadvisory.com

Font styles to use
Serif
Sans Serif

Requirements
Must have
• Our logo and the business card details.
Nice to have
• our website www.fernlowadvisory.com

```html
<!DOCTYPE html>
<html lang="en">
<head>
<meta charset="utf-8">
<title>Fernlow Advisory – Business Card</title>
<link rel="stylesheet" href="https://fonts.googleapis.com/css2?family=Open+Sans:wght@300;400;700&display=swap">
<style>
  :root {
    --backdrop: #3b3430;
    --card: #161616;
    --card-edge: #222222;
    --silver: #a9a9a9;
    --white: #f4f4f4;
    --rule: #5a5a5a;
  }
  * { margin: 0; padding: 0; box-sizing: border-box; }
  html, body { width: 1200px; height: 864px; overflow: hidden; }
  body {
    background: var(--backdrop);
    font-family: "Open Sans", Arial, sans-serif;
    display: flex;
    align-items: center;
    justify-content: center;
    gap: 40px;
  }
  .card {
    width: 540px;
    height: 309px;
    background: var(--card);
    border: 1px solid var(--card-edge);
    border-radius: 4px;
    box-shadow: 0 10px 30px rgba(0,0,0,.45);
    position: relative;
  }
  .card-front {
    display: flex;
    flex-direction: column;
    align-items: center;
    justify-content: center;
    gap: 22px;
  }
  .company-name {
    font-weight: 300;
    text-transform: uppercase;
    letter-spacing: 0.06em;
    white-space: nowrap;
  }
  .card-front .company-name { color: var(--silver); font-size: 30px; }
  .card-front .website {
    color: var(--silver);
    font-size: 12px;
    font-weight: 300;
    letter-spacing: 0.45em;
  }
  .card-back { display: flex; align-items: center; }
  .brand-side {
    width: 50%;
    display: flex;
    justify-content: center;
  }
  .card-back .company-name { color: var(--white); font-size: 20px; }
  .divider {
    width: 1px;
    height: 150px;
    background: linear-gradient(to bottom, transparent, var(--rule) 20%, var(--rule) 80%, transparent);
  }
  .contact-side {
    padding-left: 22px;
    color: var(--white);
    font-size: 13.5px;
    line-height: 1.35;
  }
  .person-name {
    font-weight: 700;
    font-size: 17px;
    text-transform: uppercase;
    margin-bottom: 8px;
    white-space: nowrap;
  }
  .address { margin-bottom: 4px; white-space: nowrap; }
  .contact-line { display: flex; align-items: center; gap: 7px; white-space: nowrap; }
  .contact-line svg { width: 10px; height: 10px; flex: none; fill: var(--white); }
</style>
</head>
<body>
  <section class="card card-front">
    <div class="company-name">Fernlow Advisory</div>
    <div class="website">www.fernlowadvisory.com</div>
  </section>

  <section class="card card-back">
    <div class="brand-side">
      <div class="company-name">Fernlow Advisory</div>
    </div>
    <div class="divider"></div>
    <div class="contact-side">
      <div class="person-name">Daniel Whitcombe</div>
      <div class="address">
        2837 North 9th Avenue<br>
        Summit Floor, Ashford Lake<br>
        Wisconsin 60483
      </div>
      <div class="contact-line">
        <svg viewBox="0 0 10 10" aria-hidden="true"><rect x="0" y="2" width="10" height="6.5" rx="0.8"/><path d="M0.5 2.6 L5 5.8 L9.5 2.6" stroke="#161616" stroke-width="0.9" fill="none"/></svg>
        <span>dan@fernlowadvisory.com</span>
      </div>
      <div class="contact-line">
        <svg viewBox="0 0 10 10" aria-hidden="true"><circle cx="5" cy="5" r="5"/><circle cx="5" cy="5" r="2" fill="#161616"/></svg>
        <span>www.fernlowadvisory.com</span>
      </div>
    </div>
  </section>
</body>
</html>
```